Fundraising team needing letterhead for sponsorship and donations

I would like a design that relates to our team name Rosy Spoke Riders. We ride in an annual bicycle event that raises money that goes towards cancer research.We already have a team jersey designed which i have attached. The team name we would prefer to be in pink. Our team includes males and females. The logo also needs to relate to bike riding.

Industry/Entity Type

Event

Font styles to use
Sans Serif

```html
<!DOCTYPE html>
<html lang="en">
<head>
<meta charset="utf-8">
<title>Rosy Spoke Riders – Letterhead</title>
<link rel="stylesheet" href="https://fonts.googleapis.com/css2?family=Cinzel:wght@500;600&family=Oswald:wght@400;600&display=swap">
<style>
  :root {
    --bg: #eeeeee;
    --paper: #ffffff;
    --pink: #e0197e;
    --pink-mid: #ee7fb4;
    --pink-band: #ec8dbb;
    --pink-band-light: #f7c9df;
    --pink-faint: #fbe6f0;
    --badge-blue: #1b4f9c;
    --badge-yellow: #f2c21b;
  }
  * { margin: 0; padding: 0; box-sizing: border-box; }
  html, body { width: 1200px; height: 1000px; overflow: hidden; }
  body {
    background: var(--bg);
    position: relative;
    font-family: "Oswald", sans-serif;
  }
  .letterhead {
    position: absolute;
    left: 279px;
    top: 50px;
    width: 643px;
    height: 900px;
    background: var(--paper);
    box-shadow: 0 2px 10px rgba(0,0,0,0.12);
    overflow: hidden;
  }
  .header-band {
    position: absolute;
    left: 0; top: 0;
    width: 643px; height: 210px;
    background: linear-gradient(to bottom,
      var(--pink-band) 0%,
      var(--pink-band-light) 45%,
      rgba(255,255,255,0) 100%);
  }
  .title {
    position: absolute;
    left: 88px;
    top: 86px;
    font-family: "Cinzel", serif;
    font-weight: 600;
    font-size: 30px;
    letter-spacing: 1px;
    color: var(--pink);
    line-height: 1;
    white-space: nowrap;
  }
  .title-reflection {
    position: absolute;
    left: 88px;
    top: 119px;
    font-family: "Cinzel", serif;
    font-weight: 600;
    font-size: 30px;
    letter-spacing: 1px;
    line-height: 1;
    white-space: nowrap;
    color: var(--pink);
    opacity: 0.15;
    transform: scaleY(-0.6);
    transform-origin: top;
  }
  .header-mark {
    position: absolute;
    right: 24px;
    top: 100px;
    font-family: "Oswald", sans-serif;
    font-weight: 600;
    font-size: 14px;
    color: var(--pink);
    display: flex;
    align-items: center;
    gap: 6px;
    white-space: nowrap;
  }
  .header-mark .dot {
    width: 10px; height: 10px; border-radius: 50%;
    background: var(--pink-mid);
  }
  .watermark {
    position: absolute;
    left: 0; right: 0;
    top: 415px;
    text-align: center;
    font-family: "Oswald", sans-serif;
    font-weight: 600;
    font-size: 54px;
    color: var(--pink-faint);
    letter-spacing: 1px;
    white-space: nowrap;
  }
  .footer {
    position: absolute;
    right: 30px;
    bottom: 26px;
    display: flex;
    align-items: flex-end;
    gap: 12px;
  }
  .footer-text {
    text-align: right;
    color: var(--pink);
    line-height: 1.15;
  }
  .footer-name { font-weight: 600; font-size: 13px; letter-spacing: 0.3px; }
  .footer-line { font-size: 9px; font-weight: 400; }
  .footer-contacts {
    display: flex;
    align-items: flex-end;
    gap: 14px;
    margin-top: 8px;
  }
  .footer-contacts .web { font-size: 9px; }
  .footer-contacts .right { text-align: right; }
  .phone { font-size: 9px; }
  .phone strong { font-size: 12px; font-weight: 600; }
  .email { font-size: 9px; }
  .partner-badge {
    width: 38px; height: 62px;
    background: var(--paper);
    border: 1px solid #c9d3e6;
    position: relative;
  }
  .partner-badge::before {
    content: "";
    position: absolute;
    left: 3px; top: 3px; right: 3px; height: 28px;
    background: var(--badge-yellow);
  }
  .partner-badge::after {
    content: "";
    position: absolute;
    left: 3px; bottom: 3px; right: 3px; height: 26px;
    background: var(--badge-blue);
  }
</style>
</head>
<body>
  <main class="letterhead">
    <div class="header-band" aria-hidden="true"></div>

    <h1 class="title">Rosy Spoke Riders</h1>
    <div class="title-reflection" aria-hidden="true">Rosy Spoke Riders</div>

    <div class="header-mark"><span class="dot"></span>Rosy Spoke Riders</div>

    <div class="watermark" aria-hidden="true">Rosy Spoke Riders</div>

    <footer class="footer">
      <div class="footer-text">
        <div class="footer-name">ROSY SPOKE RIDERS</div>
        <div class="footer-line">Fundraising bike ride for cancer research</div>
        <div class="footer-line">Organized by : Foundation Name and Address</div>
        <div class="footer-contacts">
          <span class="web">www.rosyspokeriders.org.au</span>
          <div class="right">
            <div class="phone">Phone : <strong>8225 4870 31964</strong></div>
            <div class="email">info@rosyspokeriders.org.au</div>
          </div>
        </div>
      </div>
      <div class="partner-badge" aria-hidden="true"></div>
    </footer>
  </main>
</body>
</html>
```